Corvana Wound Care Business card design

We need a business card designed around our logo which was provided. The logo of preference is the colored. Also the colors and fonts were provided.

Target Market(s)

Our Referral partners are home health agencies.

Industry/Entity Type

Healthcare

Contact Information for Business Card

Name , Phone #, Email , Title

Requirements
Nice to have
• Creativity
Should not have
• basic

```html
<!DOCTYPE html>
<html lang="en">
<head>
<meta charset="utf-8">
<title>Corvana Wound Care – Business Card</title>
<link rel="stylesheet" href="https://fonts.googleapis.com/css2?family=Poppins:wght@400;600&family=Tinos:wght@700&display=swap">
<style>
  :root {
    --navy: #06468c;
    --navy-deep: #0a3f84;
    --sky: #1a9ddc;
    --ink: #2a2a2a;
    --muted: #444;
    --card: #ffffff;
    --card-shade: #f3f5f7;
    --stage: #d2d2d2;
  }
  * { box-sizing: border-box; margin: 0; padding: 0; }
  html, body { width: 1200px; height: 889px; overflow: hidden; }
  body {
    background: radial-gradient(ellipse at 50% 45%, #ececec 0%, var(--stage) 75%);
    font-family: "Poppins", sans-serif;
    position: relative;
  }
  .card {
    position: absolute;
    width: 560px;
    height: 320px;
    background: linear-gradient(135deg, var(--card) 0%, var(--card-shade) 55%, var(--card) 100%);
    box-shadow: 0 10px 30px rgba(0,0,0,0.12);
    overflow: hidden;
  }
  .card--front { left: 60px; top: 90px; }
  .card--back { left: 580px; top: 480px; }

  .name-band {
    position: absolute;
    right: 0; top: 42px;
    width: 260px; height: 52px;
    background: var(--navy);
    border-radius: 0 0 0 14px;
    display: flex; align-items: center;
    padding-left: 20px;
  }
  .person-name {
    font-family: "Tinos", serif;
    font-weight: 700;
    font-size: 30px;
    color: #fff;
    letter-spacing: 0.5px;
    white-space: nowrap;
  }
  .designation {
    position: absolute;
    left: 320px; top: 102px;
    font-size: 14px;
    line-height: 20px;
    color: var(--muted);
  }
  .brand {
    position: absolute;
    display: flex; align-items: center; gap: 10px;
    color: var(--navy);
    font-weight: 600;
    line-height: 1;
    white-space: nowrap;
  }
  .brand__dot {
    flex: none;
    border-radius: 50%;
    background: var(--navy);
  }
  .card--front .brand { left: 50px; top: 140px; font-size: 20px; }
  .card--front .brand__dot { width: 14px; height: 14px; }
  .accent-mark {
    position: absolute;
    right: 60px; top: 190px;
    width: 56px; height: 56px;
    border-radius: 50%;
    background: linear-gradient(135deg, var(--navy-deep), var(--sky));
  }
  .contact {
    position: absolute;
    left: 60px; bottom: 36px;
    list-style: none;
    font-size: 13.5px;
    color: var(--ink);
  }
  .contact li { display: flex; align-items: center; gap: 10px; margin-top: 4px; }
  .contact svg { width: 12px; height: 12px; fill: var(--navy); flex: none; }

  .card--back .brand {
    left: 0; right: 0; top: 0; bottom: 0;
    justify-content: center;
    font-size: 34px;
    gap: 14px;
  }
  .card--back .brand__dot { width: 24px; height: 24px; }
</style>
</head>
<body>
  <section class="card card--front" aria-label="Business card front">
    <div class="name-band"><span class="person-name">Person Name</span></div>
    <p class="designation">Designation</p>
    <div class="brand"><span class="brand__dot"></span><span class="brand__name">Corvana Wound Care</span></div>
    <div class="accent-mark" aria-hidden="true"></div>
    <ul class="contact">
      <li><svg viewBox="0 0 24 24"><path d="M6.6 10.8a15 15 0 0 0 6.6 6.6l2.2-2.2a1 1 0 0 1 1-.25 11.4 11.4 0 0 0 3.6.57 1 1 0 0 1 1 1V20a1 1 0 0 1-1 1A17 17 0 0 1 3 4a1 1 0 0 1 1-1h3.5a1 1 0 0 1 1 1c0 1.25.2 2.45.57 3.57a1 1 0 0 1-.25 1z"/></svg>555-010-2468</li>
      <li><svg viewBox="0 0 24 24"><path d="M2 5h20v14H2zm2 2v.4l8 6.2 8-6.2V7l-8 6.2z"/></svg>hello@corvanacare.com</li>
      <li><svg viewBox="0 0 24 24"><path d="M12 2a10 10 0 1 0 0 20 10 10 0 0 0 0-20zm6.9 6h-2.9a15 15 0 0 0-1.4-3.6A8 8 0 0 1 18.9 8zM12 4c.8 1.2 1.5 2.5 1.9 4h-3.8c.4-1.5 1.1-2.8 1.9-4zM4.3 14a8 8 0 0 1 0-4h3.4a16 16 0 0 0 0 4zm.8 2h2.9a15 15 0 0 0 1.4 3.6A8 8 0 0 1 5.1 16zM8 8H5.1a8 8 0 0 1 4.3-3.6A15 15 0 0 0 8 8zm4 12c-.8-1.2-1.5-2.5-1.9-4h3.8c-.4 1.5-1.1 2.8-1.9 4zm2.3-6H9.7a14 14 0 0 1 0-4h4.6a14 14 0 0 1 0 4zm.3 5.6a15 15 0 0 0 1.4-3.6h2.9a8 8 0 0 1-4.3 3.6zm1.7-5.6a16 16 0 0 0 0-4h3.4a8 8 0 0 1 0 4z"/></svg>www.corvanacare.com</li>
    </ul>
  </section>

  <section class="card card--back" aria-label="Business card back">
    <div class="brand"><span class="brand__dot"></span><span class="brand__name">Corvana Wound Care</span></div>
  </section>
</body>
</html>
```